Tradeline Summit & Expo xmas banner/MREC promotion

Size:
• Leader board: 728 x 90 px
• MREC: 300 x250 px
• Half-page: 300 x 600
• Wide skyscraper: 160 x 600
Image:
Candy cane stripes as the background – image bought. Horizontal or vertical whatever you think will works.
White strip/background for the copy? See images example – unless you don’t need to do that?
Bold font which is "neutra" to our other banners attached. I think black font would look good.
Message:
Please give it a good readable pace between slides – 3 secs?
1st Slide
It’s silly season!
2nd Slide
Treat yourself to an end of year gift
3rd Slide
Book your ticket now and save $$$
4th Slide
Get spoilt. You’re worth it!
5th Slide
Tradeline logo
Target Market(s)
anyone that sells online
• Automotive • Advertising • Digital • Entertainment
• Finance • Hospitality • Pharmaceutical/Healthcare • Pop Culture
• Retail • Travel • Telecommunications

```html
<!DOCTYPE html>
<html lang="en">
<head>
<meta charset="utf-8">
<title>Silly Season Promotion</title>
<link rel="stylesheet" href="https://fonts.googleapis.com/css2?family=Josefin+Sans:wght@700&family=Source+Sans+3:wght@400&display=swap">
<style>
  :root {
    --board-dark: #1c1c1c;
    --board-mid: #2e2e2e;
    --board-light: #3a3a3a;
    --cane-red: #b3121c;
    --cane-deep: #7e0a10;
    --cane-white: #ece6e2;
    --strip-white: #ffffff;
    --ink: #111111;
    --label-bg: #000000;
    --label-text: #ffffff;
  }

  * { margin: 0; padding: 0; box-sizing: border-box; }

  html, body {
    width: 1200px;
    height: 540px;
    overflow: hidden;
  }

  .stage {
    position: relative;
    width: 1200px;
    height: 540px;
    overflow: hidden;
  }

  .wood-backdrop {
    position: absolute;
    inset: 0;
    background: linear-gradient(180deg, var(--board-mid) 0%, var(--board-dark) 45%, var(--board-light) 70%, var(--board-dark) 100%);
  }

  .mrec {
    position: absolute;
    left: 261px;
    top: 135px;
    width: 326px;
    height: 271px;
    overflow: hidden;
  }

  .candy-stripes {
    position: absolute;
    inset: 0;
    background: linear-gradient(90deg,
      var(--cane-deep) 0%, var(--cane-red) 20%, var(--cane-white) 38%,
      var(--cane-red) 55%, var(--cane-white) 72%, var(--cane-red) 88%, var(--cane-deep) 100%);
  }

  .headline-strip {
    position: absolute;
    display: flex;
    align-items: center;
    justify-content: center;
    background: var(--strip-white);
    color: var(--ink);
    font-family: "Josefin Sans", sans-serif;
    font-weight: 700;
    font-size: 35px;
    text-transform: uppercase;
    letter-spacing: 0.5px;
    line-height: 1;
    padding-top: 6px;
    transform: translate(-50%, -50%) rotate(-22.6deg);
    white-space: nowrap;
  }

  .headline-strip--top {
    left: 167px;
    top: 99px;
    width: 244px;
    height: 45px;
  }

  .headline-strip--bottom {
    left: 170px;
    top: 164px;
    width: 256px;
    height: 49px;
  }

  .description-note {
    position: absolute;
    left: 588px;
    top: 258px;
    width: 308px;
    height: 45px;
    display: flex;
    align-items: center;
    justify-content: center;
    background: var(--label-bg);
    color: var(--label-text);
    font-family: "Source Sans 3", sans-serif;
    font-weight: 400;
    font-size: 24px;
    white-space: nowrap;
  }
</style>
</head>
<body>
  <main class="stage">
    <div class="wood-backdrop" role="img" aria-label="Dark grey wooden plank backdrop"></div>

    <section class="mrec" aria-label="Christmas promotion panel">
      <div class="candy-stripes" role="img" aria-label="Photograph of red and white striped candy canes laid side by side"></div>
      <h1 class="headline-strip headline-strip--top">It’s silly</h1>
      <p class="headline-strip headline-strip--bottom">season!</p>
    </section>

    <p class="description-note">Links in the description.</p>
  </main>
</body>
</html>
```